Business Card Design Project

I want a cleaner business card and envelope then what we have now, its too crowded.
Updates

I update with logo, this can be changed anyway you feel it looks best. I also have put gaurantee on there and extended time, this is my first time doing this. Also gave an example of current card

Target Market(s)

a wide array of customers from lattice 700 to small companies and cleints

Industry/Entity Type

Business

Requirements
Must have
• Need to have address, telephone number email
Nice to have
• a sharp professional card that stands out but is still very clean.
Should not have
• Not crazy looking

```html
<!DOCTYPE html>
<html lang="en">
<head>
<meta charset="utf-8">
<title>Harbor Insurance Group – Business Cards</title>
<link href="https://fonts.googleapis.com/css2?family=Tenor+Sans&display=swap" rel="stylesheet">
<style>
  :root {
    --stage: #5a5b5d;
    --card: #ffffff;
    --ink: #3a3a3c;
    --ink-soft: #8a8a8c;
    --band: #2e2d2f;
    --mark: #9c9c9e;
    --mark-faint: #ececec;
    --rule: #6a6a6c;
  }
  html, body {
    margin: 0; padding: 0;
    width: 1200px; height: 895px;
    overflow: hidden;
    background: var(--stage);
    font-family: "Tenor Sans", sans-serif;
  }
  .sheet { position: relative; width: 1200px; height: 895px; }
  .card {
    position: absolute;
    width: 317px; height: 173px;
    background: var(--card);
    border-radius: 12px;
    overflow: hidden;
    color: var(--ink);
  }
  /* front */
  .brand { position: absolute; left: 0; right: 0; top: 32px; text-align: center; }
  .brand-square {
    width: 60px; height: 58px; margin: 0 auto 12px;
    background: var(--mark);
  }
  .brand-name { font-size: 26px; letter-spacing: 3px; line-height: 1; color: var(--ink); }
  .brand-sub { font-size: 11px; letter-spacing: 1.6px; margin-top: 3px; color: var(--ink); }
  /* back */
  .person { position: absolute; left: 16px; top: 27px; }
  .person-name { font-size: 15px; color: var(--ink); white-space: nowrap; }
  .person-role { font-size: 5px; color: var(--ink-soft); text-align: right; margin-top: 1px; }
  .contact { position: absolute; font-size: 7.5px; line-height: 11px; color: var(--ink-soft); white-space: nowrap; }
  .contact.address { text-align: right; }
  .divider { position: absolute; width: 1px; background: var(--rule); }
  .corner-square { position: absolute; right: 9px; top: 12px; width: 60px; height: 55px; background: var(--mark-faint); }
  .large-square { position: absolute; left: 109px; top: 24px; width: 130px; height: 130px; background: var(--mark-faint); }
  .web-band {
    position: absolute; left: 0; right: 0; bottom: 0; height: 20px;
    background: var(--band); color: #fff;
    font-size: 12px; letter-spacing: 0.5px;
    text-align: center; line-height: 20px;
  }
  .card > * { z-index: 1; }
</style>
</head>
<body>
<main class="sheet">

  <!-- fronts -->
  <section class="card card-front" style="left:239px; top:146px;">
    <div class="brand">
      <div class="brand-square"></div>
      <div class="brand-name">HARBOR</div>
      <div class="brand-sub">INSURANCE GROUP</div>
    </div>
  </section>
  <section class="card card-front" style="left:237px; top:381px;">
    <div class="brand">
      <div class="brand-square"></div>
      <div class="brand-name">HARBOR</div>
      <div class="brand-sub">INSURANCE GROUP</div>
    </div>
  </section>
  <section class="card card-front" style="left:239px; top:625px;">
    <div class="brand">
      <div class="brand-square"></div>
      <div class="brand-name">HARBOR</div>
      <div class="brand-sub">INSURANCE GROUP</div>
    </div>
  </section>

  <!-- backs -->
  <section class="card card-back" style="left:660px; top:146px;">
    <div class="corner-square"></div>
    <div class="person">
      <div class="person-name">Daniel Reyes</div>
      <div class="person-role">Managing Director</div>
    </div>
    <div class="contact address" style="left:16px; top:106px; text-align:left;">
      Address: 12 North Linden Road<br><span style="padding-left:32px">Oakridge, MD 21000</span>
    </div>
    <div class="contact phone" style="left:158px; top:106px;">
      Phone #: 000-000-0000<br>Fax #: 0000000000<br>Email: mail@harborgroup.com
    </div>
    <div class="web-band">www.harborgroup.com</div>
  </section>

  <section class="card card-back" style="left:658px; top:382px;">
    <div class="large-square"></div>
    <div class="person" style="top:27px;">
      <div class="person-name">Daniel Reyes</div>
      <div class="person-role">Managing Director</div>
    </div>
    <div class="contact address" style="right:160px; top:110px;">
      Address: 12 North Linden Road<br>Oakridge, MD 21000
    </div>
    <div class="divider" style="left:184px; top:108px; height:42px;"></div>
    <div class="contact phone" style="left:191px; top:110px;">
      Phone #: 000-000-0000<br>Fax #: 0000000000<br>Email: mail@harborgroup.com
    </div>
  </section>

  <section class="card card-back" style="left:660px; top:626px;">
    <div class="person">
      <div class="person-name">Daniel Reyes</div>
      <div class="person-role">Managing Director</div>
    </div>
    <div class="contact address" style="right:162px; top:110px;">
      Address: 12 North Linden Road<br>Oakridge, MD 21000
    </div>
    <div class="divider" style="left:173px; top:107px; height:42px;"></div>
    <div class="contact phone" style="left:191px; top:110px;">
      Phone #: 000-000-0000<br>Fax #: 0000000000<br>Email: mail@harborgroup.com
    </div>
  </section>

</main>
</body>
</html>
```